Law Firm Website

We are looking to update our old, tired and very flat website. We have someone who will code and host the site but we need some design inspiration. The website will consist of no more than 2/3 pages, possibly with pop-ups for information. We already have all the blurb. We would like something distinctive, clean and eye-catching, using the purple and white theme that we already use on our firm stationery. Examples uploaded. Current website URL is www.dunmorewillett.example.

Industry/Entity Type

Law Firm

```html
<!DOCTYPE html>
<html lang="en">
<head>
<meta charset="utf-8">
<title>Dunmore Willett Solicitors</title>
<link rel="stylesheet" href="https://fonts.googleapis.com/css2?family=Open+Sans:ital,wght@0,300;0,400;0,600;0,700;1,400;1,700&family=Bree+Serif&display=swap">
<style>
:root{
  --purple:#5d55a6;
  --ink:#333;
  --muted:#777;
  --line:#e3e3e3;
  --panel:#f1f1f1;
  --dark:#454545;
  --white:#fff;
}
*{margin:0;padding:0;box-sizing:border-box}
html,body{width:932px;height:1200px;overflow:hidden;background:var(--white)}
body{position:relative;font-family:"Open Sans",Arial,sans-serif;color:var(--ink)}
.abs{position:absolute}

/* header */
.brand{left:150px;top:30px;display:flex;align-items:center;gap:8px;white-space:nowrap;font-weight:700;font-size:17px;color:var(--ink)}
.brand-mark{width:12px;height:12px;background:var(--purple)}
.topbar{left:416px;top:0;width:437px;height:21px;background:#eee;font-size:7.5px;color:#333;display:flex;align-items:center;padding:0 16px;white-space:nowrap}
.topbar .welcome{flex:1}
.social{display:flex;gap:6px;margin-right:12px}
.social i{display:block;width:6px;height:6px;border-radius:50%;background:#444}
.contact-item{display:flex;align-items:center;gap:4px;margin-left:8px}
.nav{left:437px;top:43px;display:flex;gap:19px;font-size:13px;color:#333;white-space:nowrap}
.nav .active{color:var(--purple)}

/* hero */
.hero{left:0;top:91px;width:932px;height:267px;background:linear-gradient(90deg,#d9d9d9 0%,#f4f4f4 30%,#ededed 60%,#e2e2e2 100%)}
.hero-photo{left:446px;top:91px;width:486px;height:267px;background:radial-gradient(ellipse at 50% 60%,#5a5a5e 0%,#3a3a3e 35%,#cfcfcf 75%,#e6e6e6 100%)}
.hero-title{left:93px;top:173px;font-weight:300;font-size:22px;line-height:26px;color:#3a3a3a;text-transform:uppercase;white-space:nowrap}
.hero-text{left:95px;top:232px;font-size:10px;line-height:15px;color:#333;width:300px}

/* features */
.features{left:0;top:358px;width:932px;height:119px;background:var(--purple);color:var(--white)}
.feature{position:absolute;top:22px;width:210px}
.feature h3{font-family:"Bree Serif",Georgia,serif;font-weight:400;font-size:15px;display:flex;align-items:center;gap:10px;height:22px;white-space:nowrap}
.feature p{font-size:7.3px;line-height:13px;margin-top:12px;width:200px}

/* testimonial */
.quote{left:145px;top:498px;width:687px;height:70px;background:var(--panel);border-left:3px solid var(--dark)}
.quote-avatar{left:166px;top:508px;width:48px;height:48px;border-radius:50%;background:linear-gradient(#e9ddd2,#c8b4a3);border:3px solid var(--white);box-shadow:0 1px 3px rgba(0,0,0,.2)}
.quote-text{left:230px;top:510px;width:570px;font-style:italic;font-size:9.6px;line-height:17px;color:#666}
.quote-by{right:142px;top:546px;font-size:8.5px;color:#666;font-style:italic;white-space:nowrap}
.quote-by b{color:#333}
.quote-arrows{left:799px;top:549px}

/* sidebar */
.side-title{left:151px;top:577px;font-weight:700;font-style:italic;font-size:17px;color:#222}
.side-rule{left:148px;top:607px;width:151px;height:3px;background:var(--line)}
.side-list{left:148px;top:612px;width:151px;list-style:none}
.side-list li{height:26px;border-bottom:1px dashed var(--line);display:flex;align-items:center;gap:6px;font-size:8.5px;color:#666;padding-left:1px}

/* main text */
.bio{left:320px;top:575px;width:315px;font-size:8.4px;line-height:17.6px;color:#666}
.bio h2{font-weight:700;font-style:italic;font-size:21px;color:#777;line-height:28px}
.bio .gap{margin-top:17px}
.court-photo{left:646px;top:582px;width:175px;height:233px;background:linear-gradient(180deg,#5f8ac0 0%,#8fb2d9 30%,#b9aa8d 55%,#7a6c55 85%,#3d3a36 100%)}

/* footer info */
.footer-panel{left:0;top:880px;width:932px;height:246px;background:var(--panel)}
.footer-heading{font-family:"Bree Serif",Georgia,serif;font-weight:400;font-size:11px;color:#333;top:912px;text-transform:uppercase;white-space:nowrap}
.map{left:145px;top:944px;width:228px;height:149px;background:linear-gradient(135deg,#ece7df,#e3ddd2);border:3px solid var(--white);box-shadow:0 1px 3px rgba(0,0,0,.15)}
.advice{left:404px;width:260px;display:flex;gap:10px}
.advice-thumb{width:66px;height:66px;flex:none;border:3px solid var(--white);box-shadow:0 1px 3px rgba(0,0,0,.15);background:linear-gradient(180deg,#6b93c6 0%,#a7b7c7 40%,#b9a888 70%,#5d5548 100%)}
.advice h4{font-family:"Bree Serif",Georgia,serif;font-weight:400;font-size:11px;color:#333;margin-top:4px;white-space:nowrap}
.advice p{font-size:7px;line-height:11px;color:#666;margin-top:3px;width:180px}
.field{left:696px;width:136px;background:var(--white);font-size:8px;font-style:italic;color:#999;padding:5px 8px}
.send{left:764px;top:1072px;width:68px;height:22px;background:var(--dark);color:var(--white);font-size:9px;display:flex;align-items:center;justify-content:center}

/* bottom bar */
.copyright{left:145px;top:1148px;font-size:8.5px;color:#333;white-space:nowrap}
.footer-nav{right:100px;top:1148px;display:flex;gap:18px;font-size:8.5px;color:#333;white-space:nowrap}
</style>
</head>
<body>

<header>
  <div class="abs brand"><span class="brand-mark"></span>Dunmore Willett Solicitors</div>
  <div class="abs topbar">
    <span class="welcome">Welcome to our website</span>
    <span class="social"><i></i><i></i><i></i><i></i></span>
    <span class="contact-item">
      <svg width="8" height="6" viewBox="0 0 8 6"><rect width="8" height="6" fill="#444"/><path d="M0 0l4 3 4-3" stroke="#eee" fill="none" stroke-width=".8"/></svg>
      office@dunmorewillett.example
    </span>
    <span class="contact-item">
      <svg width="7" height="7" viewBox="0 0 10 10"><path d="M2 0l2 2-1 2c1 1 2 2 3 3l2-1 2 2-2 2C4 10 0 6 0 2z" fill="#444"/></svg>
      0300 555 0142
    </span>
  </div>
  <nav class="abs nav">
    <span class="active">Home</span><span>Area of Expertise</span><span>Martin Dunmore</span><span>Gareth Willett</span><span>Contact</span>
  </nav>
</header>

<section>
  <div class="abs hero"></div>
  <div class="abs hero-photo" role="img" aria-label="Photo of three solicitors in business suits standing together"></div>
  <h1 class="abs hero-title">Dunmore Willett Solicitors,<br>for the service you deserve</h1>
  <p class="abs hero-text">Lorem ipsum dolor sit amet, consectetur adipisicing elit, sed do eiusmod tempor incididunt..</p>
</section>

<section class="abs features">
  <div class="feature" style="left:145px">
    <h3><svg width="23" height="18" viewBox="0 0 23 18"><rect x="8" y="0" width="7" height="4" fill="none" stroke="#fff" stroke-width="2"/><rect x="0" y="3" width="23" height="15" rx="2" fill="#fff"/><rect x="0" y="9" width="23" height="1.5" fill="#5d55a6"/><rect x="10" y="8" width="3" height="4" fill="#5d55a6"/></svg>Solid Law Practice</h3>
    <p>Lorem ipsum dolor sit amet, consectetur adipisicing elit, sed do eiusmod tempor incididunt ut labore et dolore magna aliqua.</p>
  </div>
  <div class="feature" style="left:373px">
    <h3><svg width="14" height="20" viewBox="0 0 14 20"><path d="M7 1a6 6 0 0 0-3.5 10.8V14h7v-2.2A6 6 0 0 0 7 1z" fill="none" stroke="#fff" stroke-width="2"/><rect x="4" y="16" width="6" height="2" fill="#fff"/></svg>Creative Thinking</h3>
    <p>Lorem ipsum dolor sit amet, consectetur adipisicing elit, sed do eiusmod tempor incididunt ut labore et dolore magna aliqua.</p>
  </div>
  <div class="feature" style="left:602px">
    <h3><svg width="20" height="20" viewBox="0 0 20 20"><path d="M5 1h10v6a5 5 0 0 1-10 0z" fill="#fff"/><path d="M5 3H1c0 4 2 6 4 6M15 3h4c0 4-2 6-4 6" fill="none" stroke="#fff" stroke-width="1.6"/><rect x="9" y="12" width="2" height="4" fill="#fff"/><rect x="5" y="16" width="10" height="3" fill="#fff"/></svg>Award Winning Company</h3>
    <p>Lorem ipsum dolor sit amet, consectetur adipisicing elit, sed do eiusmod tempor incididunt ut labore et dolore magna aliqua.</p>
  </div>
</section>

<section>
  <div class="abs quote"></div>
  <div class="abs quote-avatar" role="img" aria-label="Client portrait"></div>
  <p class="abs quote-text">Ut enim ad minim veniam, quis nostrud exercitation ullamco laboris nisi ut aliquip ex ea commodo consequat. Duis aute irure dolor in reprehenderit in voluptate velit esse cillum dolore.</p>
  <p class="abs quote-by">by <b>Nora Lindqvist</b></p>
  <svg class="abs quote-arrows" width="18" height="9" viewBox="0 0 18 9"><path d="M4 1L1 4.5 4 8M14 1l3 3.5L14 8" fill="none" stroke="#333" stroke-width="1.2"/></svg>
</section>

<aside>
  <h2 class="abs side-title">Area of Expertise</h2>
  <div class="abs side-rule"></div>
  <ul class="abs side-list">
    <li><svg width="12" height="12" viewBox="0 0 12 12"><circle cx="6" cy="6" r="6" fill="#222"/><path d="M6 3v6M3 6h6" stroke="#fff" stroke-width="1.6"/></svg>Lorem ipsum dolor</li>
    <li><svg width="12" height="12" viewBox="0 0 12 12"><circle cx="6" cy="6" r="6" fill="#222"/><path d="M6 3v6M3 6h6" stroke="#fff" stroke-width="1.6"/></svg>Sit amet</li>
    <li><svg width="12" height="12" viewBox="0 0 12 12"><circle cx="6" cy="6" r="6" fill="#222"/><path d="M6 3v6M3 6h6" stroke="#fff" stroke-width="1.6"/></svg>Adipisicing elit</li>
    <li><svg width="12" height="12" viewBox="0 0 12 12"><circle cx="6" cy="6" r="6" fill="#222"/><path d="M6 3v6M3 6h6" stroke="#fff" stroke-width="1.6"/></svg>Excepteur sint occaecat</li>
  </ul>
</aside>

<article class="abs bio">
  <h2>Martin Dunmore</h2>
  <p>Martin Dunmore qualified as a solicitor in 1994 and spent over a decade advising with a growing property practice in Eastbridge.</p>
  <h2 style="margin-top:6px">Gareth Willett</h2>
  <p>Gareth Willett has 32 years experience in the law.<br>He trained in Brackenford where he advised local businesses for years and then founded his own practice in 1992 before moving on to join a regional commercial firm for 3 years.</p>
  <p class="gap">DUNMORE WILLETT is a firm of solicitors with offices in Kingsmere and Elmstead Vale. This firm is authorised and regulated by the Solicitors Standards Board, no.000417.<br>VAT registered number: 900 1234 56</p>
  <p class="gap">Professional rules can be viewed on www.ssb.example/conduct.page.</p>
</article>
<div class="abs court-photo" role="img" aria-label="Photo of a gothic stone court building under a blue sky"></div>

<section>
  <div class="abs footer-panel"></div>
  <h3 class="abs footer-heading" style="left:145px">Find our office</h3>
  <h3 class="abs footer-heading" style="left:404px">Advices &amp; best practices</h3>
  <h3 class="abs footer-heading" style="left:696px">Quick contact</h3>

  <div class="abs map" role="img" aria-label="Street map showing the office location"></div>

  <div class="abs advice" style="top:944px">
    <div class="advice-thumb" role="img" aria-label="Court building thumbnail"></div>
    <div><h4>Strategies for your Success</h4><p>Lorem ipsum dolor sit amet, consectetur elit, sed do eiusmod tempor. Officia deserunt mollit anim id est laborum reprehenderit in voluptate. sint occaecat cupidatat.</p></div>
  </div>
  <div class="abs advice" style="top:1029px">
    <div class="advice-thumb" role="img" aria-label="Court building thumbnail"></div>
    <div><h4>Strategies for your Success</h4><p>Lorem ipsum dolor sit amet, consectetur elit, sed do eiusmod tempor. Officia deserunt mollit anim id est laborum reprehenderit in voluptate. sint occaecat cupidatat.</p></div>
  </div>

  <div class="abs field" style="top:944px;height:20px">Email</div>
  <div class="abs field" style="top:974px;height:20px">Subject</div>
  <div class="abs field" style="top:1003px;height:55px">Text</div>
  <div class="abs send">Send</div>
</section>

<footer>
  <p class="abs copyright">© 2012 Copyright by DUNMORE WILLETT &nbsp;LEGAL NOTICES | PRIVACY POLICY</p>
  <nav class="abs footer-nav"><span>Home</span><span>Area of Expertise</span><span>Dunmore</span><span>Willett</span><span>news</span><span>Contact</span></nav>
</footer>

</body>
</html>
```